Cutting Edge Cloud Hosting Provider needs business card design

We are a new Cloud Hosting Provider called Verdalo Hosting. (Verdalo means cloudy in Spanish.) We provide clients with virtual resources and not virtual machines directly. Our clients purchase the resources that they will use (RAM,CPU, Hard drive space) then use those resources in as many virtual machines as they like.

We are looking for a business card design that is cutting edge and hip.
Updates

The name of the company is "Verdalo Hosting". Please include the "Hosting" part of our name in the design.

Thanks

Target Market(s)

21-35 developers and I.T. Staff

Industry/Entity Type

Business

Requirements
Must have
• Rounded corners, Must Incorporate our logo, individual's name must be prominent

```html
<!DOCTYPE html>
<html lang="en">
<head>
<meta charset="utf-8">
<title>Verdalo Hosting — Business Card</title>
<link rel="stylesheet" href="https://fonts.googleapis.com/css2?family=Cinzel:wght@400;600;700&display=swap">
<style>
  :root {
    --backdrop: #f2cd72;
    --maroon: #7a2f38;
    --maroon-deep: #5e222a;
    --rose: #f0bcc5;
    --rose-mid: #dc9ea8;
    --glow: #ffffff;
    --ink: #2a1418;
    --navy: #1f2d6b;
    --sky: #a9c6e6;
    --edge: #4a2219;
    --stripe: rgba(255, 205, 215, 0.55);
  }

  html, body {
    margin: 0;
    padding: 0;
    width: 1200px;
    height: 750px;
    overflow: hidden;
    background: var(--backdrop);
  }

  .stage {
    position: relative;
    width: 1200px;
    height: 750px;
    font-family: "Cinzel", serif;
  }

  .card {
    position: absolute;
    border-radius: 14px;
    border: 3px solid var(--edge);
    overflow: hidden;
    box-sizing: border-box;
    box-shadow: 0 6px 16px rgba(80, 40, 10, 0.25);
  }

  /* Front */
  .card--front {
    left: 200px;
    top: 74px;
    width: 416px;
    height: 250px;
    background:
      radial-gradient(circle at 30% 45%, var(--glow) 0, #fde9ed 12%, rgba(241, 195, 203, 0.9) 30%, rgba(241, 195, 203, 0) 52%),
      linear-gradient(90deg, var(--rose) 0%, var(--rose-mid) 38%, #9a4650 62%, var(--maroon) 82%, var(--maroon-deep) 100%);
  }

  .card__stripes {
    position: absolute;
    left: 0;
    top: 170px;
    width: 100%;
    height: 18px;
  }

  .card__stripes span {
    position: absolute;
    left: 0;
    width: 100%;
    height: 2px;
    background: var(--stripe);
  }
  .card__stripes span:nth-child(1) { top: 0; }
  .card__stripes span:nth-child(2) { top: 6px; height: 1px; }
  .card__stripes span:nth-child(3) { top: 12px; height: 3px; opacity: 0.7; }

  .brand {
    position: absolute;
    display: flex;
    align-items: center;
    gap: 8px;
    font-weight: 700;
    color: var(--navy);
    letter-spacing: 1px;
    line-height: 1;
    white-space: nowrap;
  }

  .brand__dot {
    flex: none;
    border-radius: 50%;
    background: var(--sky);
  }

  .card--front .brand {
    left: 16px;
    top: 82px;
    font-size: 38px;
  }
  .card--front .brand__dot { width: 18px; height: 18px; }

  .title {
    position: absolute;
    right: 18px;
    top: 22px;
    margin: 0;
    text-align: right;
    color: var(--ink);
    font-weight: 600;
    font-size: 16px;
    line-height: 1.3;
    letter-spacing: 1.5px;
    white-space: nowrap;
  }

  .address {
    position: absolute;
    right: 20px;
    top: 124px;
    margin: 0;
    text-align: right;
    color: var(--ink);
    font-size: 10px;
    line-height: 1.5;
    letter-spacing: 1px;
    font-style: normal;
    white-space: nowrap;
  }

  .contact {
    position: absolute;
    right: 18px;
    bottom: 20px;
    text-align: right;
    color: var(--ink);
    font-size: 9px;
    line-height: 1.5;
    letter-spacing: 0.5px;
    white-space: nowrap;
  }

  /* Back */
  .card--back {
    left: 706px;
    top: 322px;
    width: 442px;
    height: 308px;
    background:
      radial-gradient(circle at 50% 52%, var(--glow) 0, var(--glow) 18%, #f3e1e2 27%, #c08a90 40%, #93434c 52%, var(--maroon) 64%, var(--maroon-deep) 100%);
  }

  .card--back .brand {
    left: 50%;
    top: 50%;
    transform: translate(-50%, -50%);
    font-size: 44px;
  }
  .card--back .brand__dot { width: 20px; height: 20px; }
</style>
</head>
<body>
  <main class="stage">
    <section class="card card--front" aria-label="Business card front">
      <div class="card__stripes"><span></span><span></span><span></span></div>
      <div class="brand"><span class="brand__dot"></span><span class="brand__name">verdalo</span></div>
      <h1 class="title">Verdalo Hosting<br>Hosting Business</h1>
      <address class="address">42 Alder Row<br>Leeds</address>
      <div class="contact">
        <div>www.verdalohosting.com</div>
        <div>mail@verdalo.com</div>
      </div>
    </section>

    <section class="card card--back" aria-label="Business card back">
      <div class="brand"><span class="brand__dot"></span><span class="brand__name">verdalo</span></div>
    </section>
  </main>
</body>
</html>
```